Business Card Design Project

I am opening my own real estate company.

Tarrow & Co. Real Estate Inc.

See attachments for ideas and colors…..
Updates

Project Deadline Extended
Reason: I paid for 5 separate items (graphic design, logo, stationery, brochure & website) all at one time. I thought they all launched at the same time but they did not. That is the reason I have to extend the date.

Target Market(s)

High end real estate properties.

Industry/Entity Type

Real Estate

Font styles to use
Serif
Decorative
Script

Requirements
Must have
• High end design. I want to appeal to very expensive properties.

```html
<!DOCTYPE html>
<html lang="en">
<head>
<meta charset="utf-8">
<title>Tarrow &amp; Co. Real Estate Inc. – Business Card</title>
<link rel="stylesheet" href="https://fonts.googleapis.com/css2?family=Great+Vibes&family=Courgette&display=swap">
<style>
  :root {
    --bg-brown: #4e2200;
    --panel-brown: #5c2a02;
    --panel-edge: #7a4210;
    --inset-brown: #461d00;
    --gold: #e9c41c;
    --gold-deep: #a07a05;
    --shadow: rgba(0, 0, 0, 0.55);
  }
  html, body {
    margin: 0;
    padding: 0;
    overflow: hidden;
    background: var(--bg-brown);
  }
  .card {
    position: relative;
    width: 1200px;
    height: 720px;
    background: var(--bg-brown);
    overflow: hidden;
    font-family: "Courgette", cursive;
    color: var(--gold);
  }
  .card-line {
    position: absolute;
    margin: 0;
    line-height: 1;
    white-space: nowrap;
    text-shadow: 1px 1px 0 var(--gold-deep), 0 0 2px rgba(255, 230, 120, 0.35);
  }
  .holder-name {
    left: 142px;
    top: 104px;
    font-family: "Great Vibes", cursive;
    font-size: 78px;
  }
  .job-title   { left: 176px; top: 199px; font-size: 34px; }
  .job-amp     { left: 286px; top: 244px; font-size: 28px; }
  .industry    { left: 173px; top: 280px; font-size: 34px; }
  .contact-heading { left: 175px; top: 333px; font-size: 33px; }

  .contact-row {
    position: absolute;
    left: 173px;
    font-size: 19px;
    line-height: 1;
    text-shadow: 1px 1px 0 var(--gold-deep);
  }
  .contact-row .label { position: absolute; left: 0; }
  .contact-row .dash  { position: absolute; left: 110px; }
  .contact-row .value { position: absolute; left: 144px; white-space: nowrap; }
  .row-phone  { top: 370px; }
  .row-mobile { top: 397px; }
  .row-email  { top: 423px; }

  .address-heading { left: 158px; top: 484px; font-size: 33px; letter-spacing: 1px; }

  .brand-panel {
    position: absolute;
    left: 633px;
    top: -8px;
    width: 412px;
    height: 448px;
    background: var(--panel-brown);
    border: 1px solid var(--panel-edge);
    border-radius: 9px;
    box-shadow: 6px 8px 14px var(--shadow);
  }
  .brand-square {
    position: absolute;
    left: 88px;
    top: 138px;
    width: 237px;
    height: 160px;
    background: var(--inset-brown);
    border-radius: 6px;
  }
  .brand-name {
    position: absolute;
    left: 0;
    width: 100%;
    margin: 0;
    text-align: center;
    line-height: 1;
    color: var(--gold);
    font-family: "Courgette", cursive;
    font-weight: 400;
  }
  .brand-name-main { top: 340px; font-size: 42px; }
  .brand-name-sub  { top: 387px; font-size: 33px; }
</style>
</head>
<body>
  <main class="card">
    <section class="card-holder">
      <h1 class="card-line holder-name" style="font-weight:400">Your Name</h1>
      <p class="card-line job-title">Your Job Title</p>
      <p class="card-line job-amp">&amp;</p>
      <p class="card-line industry">Which Industry</p>
      <h2 class="card-line contact-heading" style="font-weight:400">Contect Number</h2>
      <div class="contact-row row-phone"><span class="label">Phone</span><span class="dash">-</span><span class="value">1234567890</span></div>
      <div class="contact-row row-mobile"><span class="label">Mobile</span><span class="dash">-</span><span class="value">1234567890</span></div>
      <div class="contact-row row-email"><span class="label">Email ID</span><span class="dash">-</span><span class="value">mail@tarrowco.com</span></div>
      <h2 class="card-line address-heading" style="font-weight:400">Address:-</h2>
    </section>

    <aside class="brand-panel">
      <div class="brand-square"></div>
      <p class="brand-name brand-name-main">Tarrow &amp; Co.</p>
      <p class="brand-name brand-name-sub">Real Estate Inc.</p>
    </aside>
  </main>
</body>
</html>
```